Reid Fallowmere - Senior Living Audio CDs - CD Design and Cover Design

I am an executive director in an assisted living facility. I have just started speaking, training, and coaching in the Senior Living Industry. I have 4 audio files that I want to put to a CD. The names of the CD's are:

1- Leadership - Creating A Culture of Excellence in Senior Living
2- The Purpose of Your Senior Living Business
3- A Leaders Vision - Your Attention Becomes Your Intention
4- Group Interviews -A Secret in Employee Retention

I think I can use the same CD cover for each CD. I just need the same design but 4 different ones with the names above. So everything will be the same but the name change. The inside cover will be I will consider other colors but it would be great if it would look good with the logo. I also need help with designing the CD face itself. I will be using a standard Jewel CD case. I need the front cover, the inside cover, and the back. The logo will be on all three.

On the front:

Part of me thinks it should be a clean simple design with my logo, my picture, and the title. But I am also curious about the picture of me with the elderly lady. - I need the 4 designs that are the same except the title.

On the Inside:

It can be the same design but the wording will be specific to that CD and the 4 insides will be:

All businesses rise and fall with leadership. This is especially true in the senior living industry. The life of that rise or fall is based on the culture the leader creates. Learn the 3 keys to what leaders know and do. Learn what the Importance Factor is and how you can put it to work to create and sustain a winning culture that will drive your business and occupancy above the rest.

What is the purpose of your senior living business? Your understanding to the answer of this question makes all the difference. After you have gained this understanding it takes the right beliefs and behavior of associates to fulfill this purpose. What's the purpose? How is it fulfilled?

They want a captain not a boss. As a leader in senior living you steer the ship. What you put your attention on becomes the intention of your community. Your ability to create a vision, help people embrace that vision, and learn how to stay focused when the storms of the industry come raging, is the key to your success. There is a pattern to achieving this success. Come learn this pattern and how to apply it in your life and your business. It can make all the difference.

A business can not be better than it's people. The right people are the key not just people. Learn where your focus should be to hire the right people. After you hire then find out what you can do to retain them and engage them. If you want happy residents you need happy associates.

On the back it will need to have:

1- My Logo
2- www.ReidFallowmere.example
3- Email: info@ReidFallowmere.example
4- You could put the picture of me and the elderly lady as a watermark on the back with the above info.

I have a short turn around time and need designs quickly. I also need help with designing the CD. My picture, the logo, and the Title.

```html
<!DOCTYPE html>
<html lang="en">
<head>
<meta charset="utf-8">
<title>Reid Fallowmere – Leadership CD Cover and Disc</title>
<link rel="stylesheet" href="https://fonts.googleapis.com/css2?family=Tenor+Sans&family=Nunito+Sans:wght@400&family=Lato:wght@700&display=swap">
<style>
  :root {
    --backdrop: #5d5d68;
    --sleeve-gold: #dccdaa;
    --sleeve-black: #121315;
    --sleeve-black-soft: #222428;
    --title-gold: #b4a688;
    --spine-grey: #303236;
    --label-white: #f1f1f1;
    --ink-dark: #2a2a2a;
    --disc-black: #141517;
    --disc-rim: #2e2f33;
    --hub-gold: #c9b489;
    --hub-grey: #4a4b50;
    --disc-title: #3a3b40;
    --disc-sub: #8e8674;
  }
  * { margin: 0; padding: 0; box-sizing: border-box; }
  html, body { width: 1200px; height: 959px; overflow: hidden; }
  body { background: var(--backdrop); position: relative; font-family: "Tenor Sans", sans-serif; }

  .disc { position: absolute; left: 0; top: 0; width: 1200px; height: 959px; }
  .disc-title { font-family: "Tenor Sans", sans-serif; font-size: 26px; letter-spacing: 2px; fill: var(--disc-title); }
  .disc-subtitle { font-family: "Nunito Sans", sans-serif; font-size: 14px; fill: var(--disc-sub); }
  .disc-label-name { font-family: "Tenor Sans", sans-serif; font-size: 10px; fill: var(--ink-dark); }

  .cover {
    position: absolute; left: 262px; top: 222px; width: 548px; height: 527px;
    background: var(--sleeve-gold);
  }
  .cover-panel {
    position: absolute; left: 3px; top: 21px; right: 26px; bottom: 14px;
    background: linear-gradient(160deg, var(--sleeve-black-soft) 0%, var(--sleeve-black) 55%, #0c0c0d 100%);
  }
  .series-number {
    position: absolute; left: 35px; top: 375px; transform-origin: 0 0; transform: rotate(-90deg);
    font-size: 40px; line-height: 1; letter-spacing: 4px; font-weight: 400;
    color: var(--spine-grey); white-space: nowrap;
  }
  .cover-title {
    position: absolute; left: 86px; top: 70px; font-family: "Nunito Sans", sans-serif;
    font-weight: 400; font-size: 17px; line-height: 1; color: var(--title-gold); white-space: nowrap;
  }
  .brand-tab {
    position: absolute; left: 247px; top: 315px; width: 298px; height: 89px;
    background: var(--label-white); border-radius: 14px 0 0 14px;
    display: flex; align-items: center; padding-left: 12px; gap: 9px;
  }
  .brand-dot { width: 64px; height: 64px; border-radius: 50%; background: var(--hub-gold); flex: none; }
  .brand-name { font-size: 18px; color: var(--ink-dark); line-height: 1.1; text-transform: uppercase; white-space: nowrap; }
  .brand-tagline { font-family: "Lato", sans-serif; font-weight: 700; font-size: 10px; color: var(--ink-dark); margin-top: 3px; white-space: nowrap; }
</style>
</head>
<body>
  <svg class="disc" viewBox="0 0 1200 959" aria-label="CD disc face">
    <defs>
      <radialGradient id="discShade" cx="0.45" cy="0.35" r="0.75">
        <stop offset="0" stop-color="#2a2b2f"/>
        <stop offset="1" stop-color="var(--disc-black)"/>
      </radialGradient>
      <path id="discRingTitle" d="M 1030 488 A 175 175 0 1 0 680 488 A 175 175 0 1 0 1030 488"/>
      <path id="discRingSub" d="M 1077 488 A 222 222 0 1 0 633 488 A 222 222 0 1 0 1077 488"/>
    </defs>
    <circle cx="855" cy="488" r="243" fill="#0e0e10"/>
    <circle cx="855" cy="488" r="238" fill="url(#discShade)"/>
    <circle cx="855" cy="488" r="70" fill="none" stroke="var(--disc-rim)" stroke-width="2"/>
    <circle cx="855" cy="488" r="43" fill="var(--hub-gold)"/>
    <circle cx="855" cy="488" r="35" fill="var(--hub-grey)"/>
    <circle cx="855" cy="488" r="30" fill="#3a3b40"/>
    <text class="disc-title"><textPath href="#discRingTitle" startOffset="46">1.LEADERSHIP</textPath></text>
    <text class="disc-subtitle"><textPath href="#discRingSub" startOffset="38">Creating A Culture Of Excellence In Senior Living</textPath></text>
    <path d="M 974 462 H 1093 V 520 H 974 a 14 14 0 0 1 -14 -14 V 476 a 14 14 0 0 1 14 -14 Z" fill="var(--label-white)"/>
    <circle cx="980" cy="491" r="11" fill="var(--hub-gold)"/>
    <text class="disc-label-name" x="995" y="494.5">Reid Fallowmere</text>
  </svg>

  <section class="cover" aria-label="CD front cover">
    <div class="cover-panel">
      <h2 class="series-number">1.LEADERSHIP</h2>
      <h1 class="cover-title">Creating A Culture Of Excellence In Senior Living</h1>
      <div class="brand-tab">
        <span class="brand-dot"></span>
        <div class="brand-text">
          <div class="brand-name">Reid Fallowmere</div>
          <div class="brand-tagline">Leadership Excellence In Senior Living</div>
        </div>
      </div>
    </div>
  </section>
</body>
</html>
```